3D Printing Business coming soon page

Hi we are looking for a one page "coming soon" website for our business. The business is called "Strideform Labs" and it is a new solution which 3D Prints Orthotics (Insoles).

The design should include our logo, an improved version of our promotional image (attached), a web form for capturing interest from people, a countdown timer and some text.

Follow the colour scheme which is shown in our logo along with our other colours - Orange (RGB#ff8300) and Light Green (RGB#30f20a)
Updates

Industry/Entity Type

Business

Font styles to use
Sans Serif

Requirements
Must have
• Logo (Attached)
Improved version of Promotional Image
Web Form design for capturing Name, EMail Address and Comments along with a Turin test
Countdown Timer
Text - "Strideform Labs will shake up the Orthotics Industry. Foot Orthosis patient-ready in hours for a fraction of the price you are paying today. Welcome to the new world of 3D Printing!"

Files

```html
<!DOCTYPE html>
<html lang="en">
<head>
<meta charset="utf-8">
<title>Strideform Labs — Coming Soon</title>
<link rel="stylesheet" href="https://fonts.googleapis.com/css2?family=Source+Sans+3:ital,wght@0,300;0,400;0,600;1,300;1,400&display=swap">
<style>
  :root {
    --bg: #27313b;
    --bg-light: #34404b;
    --bg-footer: #1c232a;
    --line: #3d4955;
    --text: #d7dde2;
    --muted: #b9c2c9;
    --blue: #1b9fd3;
    --blue-dark: #1675a8;
    --orange: #ff8300;
    --orange-deep: #e56a00;
    --count: #d9782a;
    --field: #5b6570;
    --field-border: #7d8790;
    --pill: #1d252d;
  }
  * { box-sizing: border-box; margin: 0; padding: 0; }
  html, body { width: 1113px; height: 1200px; overflow: hidden; }
  body {
    position: relative;
    font-family: "Source Sans 3", sans-serif;
    color: var(--text);
    background: radial-gradient(ellipse 620px 420px at 520px 300px, var(--bg-light), var(--bg) 75%);
  }
  .abs { position: absolute; }

  /* header */
  .brand { left: 230px; top: 28px; font-size: 15px; font-weight: 600; color: var(--blue); display: flex; align-items: center; gap: 7px; }
  .brand-dot { width: 14px; height: 14px; border-radius: 50%; background: var(--blue); }
  .main-nav { right: 228px; top: 30px; display: flex; gap: 0; font-size: 11px; }
  .main-nav a, .foot-nav a { color: var(--text); text-decoration: none; padding: 4px 8px; border-radius: 4px; }
  .main-nav a { padding: 4px 10px; line-height: 13px; }
  .main-nav a.active, .foot-nav a.active { background: var(--pill); box-shadow: inset 0 1px 3px rgba(0,0,0,.5); padding: 4px 13px; }
  .rule { left: 230px; width: 653px; height: 1px; background: var(--line); }

  /* hero */
  .hero-name { left: 230px; top: 280px; width: 200px; font-size: 40px; line-height: 42px; font-weight: 600; color: var(--blue); }
  .coming { left: 230px; top: 362px; font-size: 33px; font-style: italic; font-weight: 300; color: #eef2f5; }
  .countdown { left: 230px; width: 192px; top: 412px; text-align: center; font-size: 28px; color: var(--count); letter-spacing: 1px; }
  .hero-ring { left: 482px; top: 129px; width: 342px; height: 342px; border-radius: 50%;
    background: linear-gradient(160deg, #ffb21a, var(--orange) 55%, var(--orange-deep));
    box-shadow: 0 14px 22px rgba(0,0,0,.45); }
  .hero-photo { left: 499px; top: 146px; width: 308px; height: 308px; border-radius: 50%;
    background: radial-gradient(circle at 55% 45%, #c9c3bc 0 22%, #6f93b4 40%, #284d72 75%, #16304b); }
  .bubble { border-radius: 50%; background: radial-gradient(circle at 40% 35%, #35c3ef, #1284b8); box-shadow: 0 3px 6px rgba(0,0,0,.4); }
  .printer-label { left: 786px; top: 461px; font-size: 15px; color: #111; }
  .printer-arrow { left: 745px; top: 478px; }

  /* steps */
  .step { width: 144px; }
  .step-photo { height: 108px; border: 4px solid #fff; box-shadow: 0 2px 5px rgba(0,0,0,.4); }
  .step h3 { margin-top: 22px; font-size: 14px; font-weight: 600; }
  .step p { margin-top: 4px; font-size: 8.6px; line-height: 13.7px; color: var(--muted); }
  .chev { top: 622px; }
  .orange { color: var(--orange); }
  .blue { color: var(--blue); }

  /* welcome */
  .welcome { left: 231px; top: 850px; width: 310px; }
  h2 { font-size: 14px; font-weight: 400; color: var(--blue); }
  .welcome .quote { margin-top: 9px; color: var(--orange); font-size: 8.4px; line-height: 13.7px; }
  .welcome p { font-size: 8.4px; line-height: 13.7px; color: var(--muted); margin-top: 4px; }

  /* contact */
  .contact { left: 575px; top: 850px; width: 300px; }
  .field { position: absolute; left: 3px; width: 294px; background: var(--field); border: 1px solid var(--field-border);
    box-shadow: inset 0 1px 3px rgba(0,0,0,.4); font-size: 8.4px; font-style: italic; color: #d0d5da; padding: 7px 9px; }
  .captcha-code { position: absolute; left: 3px; top: 176px; font-size: 12px; font-style: italic; color: #9aa4ac; }
  .submit { position: absolute; left: 207px; top: 166px; width: 90px; height: 32px; border-radius: 3px;
    background: linear-gradient(#34b6e4, var(--blue-dark)); color: #fff; font-size: 12px; font-weight: 600;
    display: flex; align-items: center; justify-content: center; box-shadow: 0 2px 4px rgba(0,0,0,.4); }

  /* footer */
  .footer { left: 0; top: 1105px; width: 1113px; height: 95px; background: var(--bg-footer); }
  .foot-nav { left: 233px; top: 1137px; display: flex; font-size: 8.6px; line-height: 12px; }
  .foot-nav a { padding: 4px 6px; }
  .foot-nav a.active { padding: 4px 14px; margin-right: 6px; }
  .follow { left: 788px; top: 1138px; font-size: 8.6px; font-style: italic; text-decoration: underline; color: var(--muted); }
  .social { top: 1137px; width: 14px; height: 14px; border-radius: 50%; background: var(--blue-dark); }
</style>
</head>
<body>
  <!-- header -->
  <div class="abs brand"><span class="brand-dot"></span>Strideform Labs</div>
  <nav class="abs main-nav">
    <a class="active" href="#">Home</a><a href="#">About Us</a><a href="#">Services</a><a href="#">Products</a><a href="#">Contact</a>
  </nav>
  <div class="abs rule" style="top:79px"></div>

  <!-- hero -->
  <div class="abs hero-name">Strideform Labs</div>
  <div class="abs coming">Coming Soon</div>
  <div class="abs countdown">25 : 18 : 36</div>

  <div class="abs hero-ring"></div>
  <div class="abs hero-photo" role="img" aria-label="3D printer for orthotic insoles against a starry space backdrop"></div>
  <div class="abs bubble" style="left:743px;top:124px;width:20px;height:20px"></div>
  <div class="abs bubble" style="left:779px;top:133px;width:42px;height:42px"></div>
  <div class="abs bubble" style="left:811px;top:161px;width:78px;height:78px"></div>

  <div class="abs printer-label">Strideform Printer</div>
  <svg class="abs printer-arrow" width="60" height="26" viewBox="0 0 60 26">
    <path d="M58 8 C50 24 20 24 6 12" fill="none" stroke="#111" stroke-width="2"/>
    <path d="M6 12 L7 3 M6 12 L15 13" fill="none" stroke="#111" stroke-width="2"/>
  </svg>

  <div class="abs rule" style="top:543px"></div>

  <!-- steps -->
  <div class="abs step" style="left:230px;top:577px">
    <div class="step-photo" role="img" aria-label="Tablet with attached foot scanner" style="background:linear-gradient(#fff,#d8d8d8)"></div>
    <h3 class="orange">Scan the Foot</h3>
    <p>Lorem ipsum dolor sit amet, consectetur adipisicing elit, sed do eiusmod tempor incididunt ut labore et dolore magna aliqua.</p>
  </div>
  <div class="abs step" style="left:399px;top:577px">
    <div class="step-photo" role="img" aria-label="Foot resting above a custom orthotic insole" style="background:linear-gradient(#e9dccd,#c9a27c 55%,#f3efe9)"></div>
    <h3 class="blue">Design the Orthotic</h3>
    <p>Lorem ipsum dolor sit amet, consectetur adipisicing elit, sed do eiusmod tempor incididunt ut labore et dolore magna aliqua.</p>
  </div>
  <div class="abs step" style="left:570px;top:577px">
    <div class="step-photo" role="img" aria-label="3D printer producing the insole" style="background:linear-gradient(#f3f3f3,#d9d4cc)"></div>
    <h3 class="orange">3D Print it</h3>
    <p>Lorem ipsum dolor sit amet, consectetur adipisicing elit, sed do eiusmod tempor incididunt ut labore et dolore magna aliqua.</p>
  </div>
  <div class="abs step" style="left:739px;top:577px">
    <div class="step-photo" role="img" aria-label="Hand fitting an insole into a running shoe" style="background:linear-gradient(#e6e6e6,#9a9a9a)"></div>
    <h3 class="blue">Fit it</h3>
    <p>Lorem ipsum dolor sit amet, consectetur adipisicing elit, sed do eiusmod tempor incididunt ut labore et dolore magna aliqua.</p>
  </div>
  <svg class="abs chev" style="left:383px" width="10" height="20"><path d="M2 1 L8 10 L2 19" fill="none" stroke="#c9d0d6" stroke-width="1.2"/></svg>
  <svg class="abs chev" style="left:553px" width="10" height="20"><path d="M2 1 L8 10 L2 19" fill="none" stroke="#c9d0d6" stroke-width="1.2"/></svg>
  <svg class="abs chev" style="left:723px" width="10" height="20"><path d="M2 1 L8 10 L2 19" fill="none" stroke="#c9d0d6" stroke-width="1.2"/></svg>

  <div class="abs rule" style="top:817px"></div>

  <!-- welcome -->
  <section class="abs welcome">
    <h2>Welcome to our site</h2>
    <p class="quote">"Strideform Labs will shake up the Orthotics Industry. Foot Orthosis patient-ready in hours for a fraction of the price you are paying today. Welcome to the new world of 3D Printing!"</p>
    <p>Lorem ipsum dolor sit amet, consectetur adipisicing elit, sed do eiusmod tempor incididunt ut labore et dolore magna aliqua. Lorem ipsum dolor sit amet, consectetur adipisicing elit, sed do eiusmod tempor incididunt ut labore et dolore magna aliqua.</p>
    <p>Lorem ipsum dolor sit amet, consectetur adipisicing elit, sed do eiusmod tempor incididunt ut labore et dolore magna aliqua. Lorem ipsum dolor sit amet, consectetur adipisicing elit, sed do eiusmod tempor incididunt ut labore et dolore magna aliqua. Lorem ipsum dolor sit amet, consectetur adipisicing elit, sed do eiusmod tempor incididunt ut labore et dolore magna aliqua.</p>
  </section>

  <!-- contact -->
  <section class="abs contact">
    <h2>Contact Us</h2>
    <div class="field" style="top:25px;height:25px">Your Name</div>
    <div class="field" style="top:57px;height:25px">Email Address</div>
    <div class="field" style="top:88px;height:68px">Comments</div>
    <div class="captcha-code">kfi5fld</div>
    <div class="field" style="left:45px;top:167px;width:95px;height:30px;padding-top:10px">Type the given text here</div>
    <div class="submit">Submit</div>
  </section>

  <!-- footer -->
  <footer class="abs footer"></footer>
  <nav class="abs foot-nav">
    <a class="active" href="#">Home</a><a href="#">About Us</a><a href="#">Service</a><a href="#">Product</a><a href="#">Contact</a>
  </nav>
  <div class="abs follow">Follow Us :</div>
  <div class="abs social" style="left:836px"></div>
  <div class="abs social" style="left:858px;background:var(--blue)"></div>
</body>
</html>
```